Tallow Crest Business Card

We need a business card designed for a a company called "Tallow Crest". We offer consulting, coaching and training to business leaders and coaches (across the world) using the latest findings in neuroscience, social and emotional intelligence and positive psychology. The final design should communicate the use of brain science to create sustainable relationships.

The card should be doublesided. The logo is attached and names and titles will be provided to the successful designer. Thank you.

Industry/Entity Type

Training

```html
<!DOCTYPE html>
<html lang="en">
<head>
<meta charset="utf-8">
<title>Tallow Crest Business Card</title>
<link rel="stylesheet" href="https://fonts.googleapis.com/css2?family=Comfortaa:wght@300;400;700&display=swap">
<style>
  :root {
    --card-bg: #231f20;
    --page-bg: #ffffff;
    --brand-blue: #0092c8;
    --brand-green: #c4d82e;
    --ink-light: #ececec;
    --ink-soft: #d6d6d6;
    --ghost: #2c2a2b;
  }
  * { margin: 0; padding: 0; box-sizing: border-box; }
  html, body { width: 1200px; height: 878px; overflow: hidden; background: var(--page-bg); }
  body { position: relative; font-family: "Comfortaa", sans-serif; }

  .card {
    position: absolute;
    top: 0;
    width: 545px;
    height: 878px;
    background: var(--card-bg);
    overflow: hidden;
  }
  .card--front { left: 18px; }
  .card--back { left: 628px; }

  /* Front: brand block */
  .brand {
    position: absolute;
    top: 168px;
    left: 0;
    width: 100%;
    text-align: center;
  }
  .brand__mark {
    display: block;
    width: 170px;
    height: 170px;
    margin: 0 auto 56px;
    background: var(--brand-blue);
    border-radius: 20px;
  }
  .brand__name {
    color: var(--brand-blue);
    font-weight: 700;
    font-size: 64px;
    line-height: 1.1;
    letter-spacing: 2px;
  }

  /* Front: contact list */
  .contacts {
    position: absolute;
    left: 46px;
    top: 718px;
    list-style: none;
  }
  .contacts__item {
    display: flex;
    align-items: center;
    height: 48px;
    color: var(--ink-light);
    font-size: 29px;
    font-weight: 400;
  }
  .contacts__icon {
    width: 26px;
    height: 26px;
    margin-right: 18px;
    flex: none;
  }
  .contacts__icon--square { background: var(--ink-soft); border-radius: 3px; }

  /* Back */
  .ghost-mark {
    position: absolute;
    left: 50%;
    top: 150px;
    width: 440px;
    height: 440px;
    margin-left: -220px;
    border-radius: 50%;
    background: var(--ghost);
  }
  .person {
    position: absolute;
    top: 328px;
    left: 0;
    width: 100%;
    text-align: center;
  }
  .person__name {
    font-size: 38px;
    font-weight: 700;
  }
  .person__first { color: var(--brand-green); }
  .person__last { color: var(--brand-blue); }
  .person__title {
    margin-top: 30px;
    color: var(--ink-light);
    font-size: 33px;
    font-weight: 400;
    letter-spacing: 1px;
  }
  .address {
    position: absolute;
    bottom: 20px;
    left: 0;
    width: 100%;
    text-align: center;
    color: var(--ink-soft);
    font-size: 28px;
    font-weight: 300;
    line-height: 46px;
  }
</style>
</head>
<body>
  <section class="card card--front">
    <div class="brand">
      <span class="brand__mark"></span>
      <p class="brand__name">TALLOW<br>CREST</p>
    </div>
    <ul class="contacts">
      <li class="contacts__item"><span class="contacts__icon contacts__icon--square"></span>/deranaksoy</li>
      <li class="contacts__item"><span class="contacts__icon contacts__icon--square"></span>@deran.aksoy</li>
      <li class="contacts__item">
        <svg class="contacts__icon" viewBox="0 0 26 26" aria-hidden="true">
          <rect x="2" y="5" width="22" height="16" rx="1.5" fill="none" stroke="#d6d6d6" stroke-width="2"/>
          <path d="M3 6 L13 14 L23 6" fill="none" stroke="#d6d6d6" stroke-width="2"/>
        </svg>deran.aksoy@tallowcrest.com
      </li>
    </ul>
  </section>

  <section class="card card--back">
    <span class="ghost-mark"></span>
    <div class="person">
      <p class="person__name"><span class="person__first">Deran</span> <span class="person__last">AKSOY</span></p>
      <p class="person__title">DESIGNER</p>
    </div>
    <p class="address">Kavak Mh. Lale Cd. Ada Sk. 34720<br>Istanbul/TURKEY.</p>
  </section>
</body>
</html>
```